Sol Bocado Digital Menu Boards

IF SELECTED, WINNER MAY BE HIRED FOR OTHER DESIGNS OF DIFFERENT STORES OF OUR COMPANY.

Task: Digital Menu Boards Design

Task description: We need designs for a Digital Menu to be displayed on two 42’’screens at Solbocado, a fast-food restaurant in Guadalajara, Mexico. The menu redesign should communicate to our customers the experience of eating at our restaurant.

For avoiding the creation of videos, we are expecting several menu slides with the same text but with different images, simulating the effect of a video where the images are changing. This menu slides will be projected through a USB memory and a slideshow.

Attached files:
For the design, there are several documents attached to the task description:
1. Logo of the restaurant
2. Pictures of the restaurant
3. Example video of what we want to achieve through this menu slides.
4. Pictures of the actual menu board, to be replaced with the new designs.
5. Menu description (regular and breakfast menu)
6. Pictures of each element on the menu (We don’t have yet any breakfast pictures)
**The files are organized on a ZIP file.

Expected product:
For the regular menu,
• 2 menu slide designs for TACOS Y ESPECIALIDADES, where the text will be exactly the same but the images would differ.
• 2 menu slide designs for BEBIDAS Y EXTRAS, where the text will be exactly the same but the images would differ.
For the breakfast menu,
• 1 menu slide including all the menu
Total: 5 menu board slides.

Technical specs:
• You should send the editable file, med and high resolution JPGs for each design.
• The designs should fit perfectly on 42’’ screens.

Reason: Designers, For the final decision we are asking for a minimum of designs for chosing, we are going to wait a little bit more. Solbocado

Industry/Entity Type

Restaurant

```html
<!DOCTYPE html>
<html lang="es">
<head>
<meta charset="utf-8">
<title>Sol Bocado – Tacos y Especialidades</title>
<link rel="stylesheet" href="https://fonts.googleapis.com/css2?family=Bebas+Neue&display=swap">
<style>
  :root {
    --wood-dark: #3a2212;
    --wood-mid: #6b4426;
    --wood-light: #9a6a3e;
    --banner-red: #b81e2a;
    --banner-deep: #8e1520;
    --text-light: #fbf4e8;
    --header-ink: #2b1a0e;
    --header-glow: rgba(255, 236, 200, 0.75);
    --food-warm: #c98a4e;
    --food-cream: #eadcc0;
    --brand-sun: #f2c94c;
  }
  * { margin: 0; padding: 0; box-sizing: border-box; }
  html, body { width: 1200px; height: 762px; overflow: hidden; background: var(--wood-dark); }
  .menu-board {
    position: relative;
    width: 1200px;
    height: 762px;
    overflow: hidden;
    font-family: "Bebas Neue", "Arial Narrow", sans-serif;
    color: var(--text-light);
    background:
      radial-gradient(ellipse 60% 55% at 60% 60%, var(--wood-light) 0%, var(--wood-mid) 45%, var(--wood-dark) 100%);
  }
  .title-banner {
    position: absolute;
    top: 0;
    left: 387px;
    width: 813px;
    height: 150px;
  }
  .title-banner svg { position: absolute; inset: 0; }
  .title-banner h1 {
    position: relative;
    font-weight: 400;
    font-size: 78px;
    letter-spacing: 2px;
    line-height: 1;
    padding: 28px 0 0 36px;
    color: var(--text-light);
    text-shadow: 2px 3px 0 rgba(0, 0, 0, 0.35);
    transform: rotate(-1.5deg);
    transform-origin: left top;
  }
  .hero-photo {
    position: absolute;
    left: 0;
    top: 132px;
    width: 440px;
    height: 300px;
    border-radius: 0 50% 50% 0 / 0 45% 45% 0;
    background: radial-gradient(ellipse at 60% 50%, var(--food-cream) 0%, var(--food-warm) 55%, rgba(107, 68, 38, 0) 100%);
  }
  .dish-thumb {
    position: absolute;
    top: 212px;
    width: 160px;
    height: 118px;
    border-radius: 50%;
    background: radial-gradient(ellipse at 50% 55%, var(--food-warm) 0%, rgba(150, 90, 50, 0.6) 50%, rgba(107, 68, 38, 0) 75%);
  }
  .col-header, .price {
    position: absolute;
    width: 190px;
    margin-left: -95px;
    text-align: center;
    line-height: 1;
  }
  .col-header {
    top: 352px;
    font-size: 46px;
    color: var(--header-ink);
    text-shadow: 0 0 6px var(--header-glow), 0 0 2px var(--header-glow);
  }
  .col-header span {
    display: inline-block;
    border-bottom: 3px solid var(--header-ink);
    padding-bottom: 2px;
    box-shadow: 0 2px 4px -2px var(--header-glow);
  }
  .row-label {
    position: absolute;
    right: 696px;
    font-size: 29px;
    line-height: 1;
    letter-spacing: 0.5px;
    text-shadow: 1px 2px 3px rgba(0, 0, 0, 0.5);
    white-space: nowrap;
  }
  .price {
    font-size: 46px;
    text-shadow: 2px 3px 3px rgba(0, 0, 0, 0.55);
  }
  .brand {
    position: absolute;
    left: 40px;
    top: 560px;
    display: flex;
    align-items: center;
    gap: 14px;
  }
  .brand-dot {
    width: 64px;
    height: 64px;
    border-radius: 50%;
    background: var(--brand-sun);
  }
  .brand-name {
    font-size: 50px;
    line-height: 1;
    color: var(--text-light);
  }
</style>
</head>
<body>
<main class="menu-board">

  <header class="title-banner">
    <svg viewBox="0 0 813 150" width="813" height="150" preserveAspectRatio="none" aria-hidden="true">
      <polygon fill="var(--banner-red)"
        points="0,0 813,0 813,128 790,122 768,134 744,120 720,138 700,126 676,140 650,124 628,132 604,118 580,136 556,122 532,142 508,126 482,134 460,120 436,140 412,126 388,134 362,118 340,138 316,124 292,132 268,116 246,136 222,122 198,132 174,118 150,136 126,122 102,130 78,116 54,134 30,120 0,130" />
      <polygon fill="var(--banner-deep)" opacity="0.5"
        points="0,118 30,112 54,124 78,106 102,120 126,112 150,126 174,108 198,122 222,112 246,126 268,106 292,122 316,114 340,128 362,108 388,124 412,116 436,130 460,110 482,124 508,116 532,132 556,112 580,126 604,108 628,122 650,114 676,130 700,116 720,128 744,110 768,124 790,112 813,118 813,128 790,122 768,134 744,120 720,138 700,126 676,140 650,124 628,132 604,118 580,136 556,122 532,142 508,126 482,134 460,120 436,140 412,126 388,134 362,118 340,138 316,124 292,132 268,116 246,136 222,122 198,132 174,118 150,136 126,122 102,130 78,116 54,134 30,120 0,130" />
    </svg>
    <h1>Tacos y Especialidades</h1>
  </header>

  <div class="hero-photo" role="img" aria-label="Foto de tacos de pastor y arrachera con queso, guacamole y pico de gallo"></div>

  <div class="dish-thumb" style="left:482px" role="img" aria-label="Foto de tacos"></div>
  <div class="dish-thumb" style="left:657px" role="img" aria-label="Foto de quesadilla"></div>
  <div class="dish-thumb" style="left:847px" role="img" aria-label="Foto de volcán"></div>
  <div class="dish-thumb" style="left:1015px" role="img" aria-label="Foto de gringa"></div>

  <h2 class="col-header" style="left:562px"><span>Tacos</span></h2>
  <h2 class="col-header" style="left:737px"><span>Quesadilla</span></h2>
  <h2 class="col-header" style="left:927px"><span>Volcán</span></h2>
  <h2 class="col-header" style="left:1095px"><span>Gringa</span></h2>

  <p class="row-label" style="top:472px">Pastor</p>
  <p class="row-label" style="top:570px">Arrachera</p>
  <p class="row-label" style="top:668px">Tortilla de harina</p>

  <p class="price" style="left:562px; top:466px">14</p>
  <p class="price" style="left:737px; top:460px">18</p>
  <p class="price" style="left:927px; top:456px">18</p>
  <p class="price" style="left:1095px; top:450px">20</p>

  <p class="price" style="left:562px; top:566px">16</p>
  <p class="price" style="left:737px; top:562px">20</p>
  <p class="price" style="left:927px; top:558px">20</p>
  <p class="price" style="left:1095px; top:554px">22</p>

  <p class="price" style="left:562px; top:664px">+1</p>
  <p class="price" style="left:737px; top:662px">+1</p>
  <p class="price" style="left:927px; top:660px">+1</p>
  <p class="price" style="left:1095px; top:656px">+2</p>

  <div class="brand">
    <span class="brand-dot" aria-hidden="true"></span>
    <span class="brand-name">Sol Bocado</span>
  </div>

</main>
</body>
</html>
```